Wordpress website design for Tavi Linkway-Africa

We need a website for a new consultancy and digital marketplace in Kenya called 'Tavi Linkway - Africa'. Please refer to the the attached document [Tavi Linkway Africa website brief] and contact me anytime.

Bests,
Philippa

Deadline extended to allow for additional revisions and refinements, ensuring that final designs align closely with project objectives and quality standards. This extra time will help incorporate valuable feedback and ensure the final output meets our high expectations.

```html
<!DOCTYPE html>
<html lang="en">
<head>
<meta charset="utf-8">
<title>Tavi Linkway Africa – Digital Marketplace</title>
<link rel="stylesheet" href="https://fonts.googleapis.com/css2?family=Poppins:wght@400;500;600;700;800&display=swap">
<style>
:root{
  --green:#2a9c2f;
  --green-dark:#1f7f26;
  --green-light:#3fb13c;
  --blue:#1a6fd0;
  --navy:#1a3584;
  --navy-deep:#142a6b;
  --text:#1d1d1f;
  --muted:#6b6f76;
  --line:#2b6fc0;
  --white:#ffffff;
}
*{box-sizing:border-box;margin:0;padding:0}
html,body{width:1200px;height:4743px;overflow:hidden}
body{font-family:'Poppins',sans-serif;color:var(--text);background:var(--white);position:relative}
section,header,footer{position:absolute;left:0;width:1200px}
.abs{position:absolute}
.btn{position:absolute;display:flex;align-items:center;justify-content:center;border-radius:30px;font-weight:700;font-size:14px;letter-spacing:.3px;text-transform:uppercase}
.btn-green{background:var(--green);color:var(--white)}
.btn-blue{background:var(--blue);color:var(--white)}
.section-title{position:absolute;font-weight:700;font-size:45px;line-height:1}
.placeholder{position:absolute}

/* hero */
.hero{top:0;height:729px;background:linear-gradient(100deg,#4f8f58 0%,#3d9a44 35%,#2ea33a 60%,#23992f 100%);overflow:hidden}
.hero-fade{position:absolute;inset:0;background:linear-gradient(90deg,rgba(60,110,70,.55) 0%,rgba(46,150,56,.2) 55%,rgba(42,160,50,0) 100%)}
.hero-arc{position:absolute;right:-160px;top:-120px;width:900px;height:900px;border-radius:50%;background:#27a233}
.topbar{position:absolute;left:88px;top:28px;width:1024px;height:92px;background:var(--white);border-radius:8px}
.brand{position:absolute;left:20px;top:22px}
.brand-name{font-weight:700;font-size:23px;color:var(--blue);line-height:1.1}
.brand-tag{font-size:9px;letter-spacing:2.6px;color:var(--muted);font-weight:500;margin-top:2px}
.nav{position:absolute;left:309px;top:35px;display:flex;gap:25px;font-size:14.5px;font-weight:500}
.nav .active{color:var(--blue)}
.icon-btn{position:absolute;top:24px;width:44px;height:44px;border-radius:50%;display:flex;align-items:center;justify-content:center}
.hero-kicker{left:88px;top:337px;color:var(--white);font-weight:600;font-size:22px}
.hero-title{left:88px;top:368px;color:var(--white);font-weight:800;font-size:60px;line-height:63px}
.connect{left:88px;top:648px;color:var(--white);font-size:10px;letter-spacing:2.4px;font-weight:600}
.hero-social{left:88px;top:675px;display:flex;gap:28px}
.hero-social span{width:14px;height:14px;border-radius:50%;background:var(--white);display:block}
.hero-dots{left:1107px;top:369px;display:flex;flex-direction:column;gap:9px}
.hero-dots span{width:9px;height:9px;border-radius:50%;background:rgba(255,255,255,.6)}
.hero-dots span:first-child{background:var(--white)}

/* intro */
.intro{top:729px;height:697px}
.intro p{position:absolute;left:556px;width:556px;font-size:14px;line-height:28.5px;color:var(--muted);text-align:justify}
.brand-box{left:340px;top:383px;width:135px;height:213px;border-radius:8px;background:linear-gradient(160deg,#2aa23a,#1a6fd0);display:flex;align-items:center;justify-content:center}
.brand-box .v{transform:rotate(-90deg);color:var(--white);text-align:center;white-space:nowrap}
.brand-box .v b{display:block;font-size:24px;font-weight:700;line-height:1}
.brand-box .v small{display:block;font-size:8.5px;letter-spacing:2.3px;margin-top:5px}
.aim{left:556px;top:508px;display:flex;gap:16px;align-items:center}
.aim-text{font-weight:600;font-size:14.5px;line-height:28px;color:#343a40;border-left:2px solid var(--green);padding-left:16px}

/* services */
.services{top:1426px;height:738px;background:linear-gradient(160deg,#234a9e 0%,#1d3d92 45%,#162f78 100%);overflow:hidden}
.services .section-title{left:0;width:1200px;text-align:center;top:91px;color:var(--white)}
.services .section-title em{font-style:normal;color:var(--green-light)}
.cards{position:absolute;left:88px;top:184px;display:flex;gap:14px}
.svc{width:246px;height:368px;background:var(--white);border-radius:6px;position:relative;padding:28px 26px}
.svc.featured{background:linear-gradient(160deg,#1a6fd0 0%,#219a4a 55%,#26a03a 100%);color:var(--white)}
.svc h3{position:absolute;top:115px;left:26px;font-size:21px;line-height:29px;font-weight:700}
.svc p{position:absolute;top:188px;left:26px;width:200px;font-size:14px;line-height:28.5px;color:var(--muted)}
.svc.featured p{color:var(--white)}
.svc .arrow{position:absolute;left:26px;top:290px;width:52px;height:52px;border-radius:50%;background:var(--green);display:flex;align-items:center;justify-content:center}
.svc.featured .arrow{background:var(--blue)}

/* values */
.values{top:2164px;height:744px}
.values .section-title{left:88px;top:418px;color:var(--blue)}
.values-intro{left:88px;top:488px;width:380px;font-size:14.5px;line-height:28.5px;color:var(--muted)}
.value{position:absolute;left:580px;width:532px}
.value .circle{position:absolute;left:0;width:114px;height:114px;border-radius:50%;display:flex;align-items:center;justify-content:center}
.value h4{position:absolute;left:143px;font-size:20px;font-weight:600}
.value p{position:absolute;left:143px;width:389px;font-size:14.5px;line-height:28.5px;color:var(--muted)}
.value hr{position:absolute;left:143px;width:389px;border:0;border-top:2px solid var(--line)}

/* products */
.products{top:2908px;height:760px;background:linear-gradient(140deg,#2f9c3b 0%,#2aa33a 50%,#1f9129 100%);overflow:hidden}
.products .section-title{left:0;width:1200px;text-align:center;top:106px;color:var(--white)}
.prod-row{position:absolute;left:138px;top:186px;display:flex;gap:18px}
.prod{width:297px;height:482px;background:var(--white);border-radius:6px;overflow:hidden;position:relative;text-align:center}
.prod .shot{height:208px;width:100%}
.prod h3{margin-top:20px;font-size:20px;font-weight:600}
.stars{margin-top:2px;display:flex;justify-content:center;gap:6px;align-items:center;font-size:13px;color:var(--muted)}
.prod p{margin:10px auto 0;width:250px;font-size:14px;line-height:28.5px;color:var(--muted)}
.prod .rule{width:200px;margin:14px auto 0;border-top:2px solid #a9c7ee}
.price{margin-top:10px;font-size:13px;color:var(--muted)}
.price b{font-size:18px;color:var(--blue);font-weight:700}
.prod .buy{position:relative;margin:17px auto 0;width:172px;height:48px;border:2px solid var(--green);color:var(--green);border-radius:30px;font-weight:700;font-size:14px;display:flex;align-items:center;justify-content:center}
.prod .buy.solid{background:var(--green);color:var(--white)}
.slide-btn{position:absolute;top:394px;width:66px;height:66px;border-radius:50%;border:2px solid var(--white);display:flex;align-items:center;justify-content:center}

/* team */
.team{top:3668px;height:552px}
.team .section-title{left:88px;top:92px;color:var(--blue)}
.member{position:absolute;top:186px;width:250px;text-align:center}
.member .avatar{width:173px;height:173px;border-radius:50%;margin:0 auto}
.member h4{margin-top:20px;font-size:21px;font-weight:600}
.member p{margin-top:4px;font-size:14.5px;line-height:28.5px;color:var(--muted)}

/* footer */
.site-footer{top:4220px;height:523px;background:linear-gradient(160deg,#213f8e 0%,#1a3584 50%,#142a6b 100%);color:var(--white)}
.f-brand{left:88px;top:140px}
.f-brand .brand-name{color:var(--blue);font-size:24px}
.f-brand .brand-tag{color:#8c97b8}
.f-social{left:88px;top:212px;display:flex;gap:10px}
.f-social span{width:44px;height:44px;border-radius:50%;background:var(--green);display:flex;align-items:center;justify-content:center}
.f-social span i{width:14px;height:14px;border-radius:50%;border:2px solid var(--white);display:block}
.f-col{position:absolute;top:74px}
.f-col h5{font-size:19px;font-weight:600}
.f-col h5::after{content:"";display:block;width:34px;height:2px;background:var(--green);margin-top:6px}
.f-col ul{list-style:none;margin-top:14px;font-size:15px;line-height:36.5px}
.contact-item{display:flex;gap:14px;font-size:15px;line-height:23px;margin-top:14px}
.contact-item svg{flex:none;margin-top:3px}
.copyright{position:absolute;left:0;width:1200px;bottom:18px;text-align:center;font-size:14px;font-weight:500}
</style>
</head>
<body>

<header class="hero">
  <div class="hero-arc"></div>
  <div class="hero-fade" role="img" aria-label="Faded photo of a team at work in an office"></div>
  <div class="placeholder" style="left:585px;top:135px;width:430px;height:594px;background:linear-gradient(180deg,#6aa06d 0%,#3a6b8e 55%,#2b4e7c 100%);border-radius:200px 200px 0 0;opacity:.85" role="img" aria-label="Photo of two smiling professionals, a man holding a phone and a woman holding a coffee cup and laptop"></div>

  <div class="topbar">
    <div class="brand">
      <div class="brand-name">Tavi Linkway</div>
      <div class="brand-tag">A DIGITAL MARKETPLACE</div>
    </div>
    <nav class="nav">
      <span class="active">Home</span><span>Services</span><span>Digital Marketplace</span><span>About Us</span><span>Blog</span><span>Contact</span>
    </nav>
    <div class="icon-btn" style="left:900px;border:2px solid var(--blue)">
      <svg width="20" height="20" viewBox="0 0 20 20" fill="none" stroke="#1a6fd0" stroke-width="1.8"><circle cx="10" cy="7" r="3.5"/><path d="M3.5 18c.8-4 3.5-5.5 6.5-5.5s5.7 1.5 6.5 5.5"/></svg>
    </div>
    <div class="icon-btn" style="left:956px;background:var(--green)">
      <svg width="20" height="20" viewBox="0 0 20 20" fill="none" stroke="#fff" stroke-width="1.8"><path d="M2 3h3l2 10h9l2-7H6"/><circle cx="8" cy="16.5" r="1.2"/><circle cx="15" cy="16.5" r="1.2"/></svg>
    </div>
  </div>

  <div class="abs hero-kicker">Empowering Innovations &amp; Digital</div>
  <h1 class="abs hero-title">Transformation<br>Across Africa</h1>
  <div class="btn btn-green" style="left:88px;top:524px;width:170px;height:48px">Get Started</div>
  <div class="abs connect">CONNECT WITH US</div>
  <div class="abs hero-social"><span></span><span></span><span></span><span></span></div>
  <div class="abs hero-dots"><span></span><span></span><span></span></div>
</header>

<section class="intro">
  <div class="placeholder" style="left:88px;top:94px;width:387px;height:280px;border-radius:8px;background:linear-gradient(135deg,#8a8f96,#4d5560)" role="img" aria-label="Photo of colleagues discussing work at a desk"></div>
  <div class="placeholder" style="left:108px;top:313px;width:231px;height:284px;border-radius:8px;border:5px solid #fff;background:linear-gradient(160deg,#c9c3bd,#6f655e)" role="img" aria-label="Portrait photo of a smiling woman with glasses"></div>
  <div class="abs brand-box"><div class="v"><b>Tavi Linkway</b><small>A DIGITAL MARKETPLACE</small></div></div>

  <h2 class="section-title" style="left:556px;top:92px;color:var(--blue)">Our Introduction</h2>
  <p style="top:152px">Tavi Linkway Africa is a consultancy firm and digital marketplace dedicated to supporting Africa’s digital transformation. We provide data-driven insights, strategic guidance, customised solutions to empower public and private sectors.</p>
  <p style="top:294px">Our marketplace offers a curated selection of digital products and tools designed to support strategic growth, expand knowledge, strengthen data capabilities, and streamline operations. With deep expertise in digital transformation and a focus on Africa’s unique opportunities, Tavi Linkway Africa is your trusted partner in navigating today’s dynamic digital landscape.</p>
  <div class="abs aim">
    <svg width="86" height="86" viewBox="0 0 86 86" fill="none" stroke="#2a9c2f" stroke-width="2.4"><circle cx="44" cy="36" r="18"/><circle cx="44" cy="36" r="7"/><path d="M44 12v-6M44 66v-6M20 36h-6M74 36h-6M27 19l-4-4M61 53l4 4M61 19l4-4M27 53l-4 4"/><path d="M36 60h16v8H36zM39 72h10"/></svg>
    <div class="aim-text">We aim to tackle complex challenges, optimize<br>operations, and unlock growth through<br>innovative technology.</div>
  </div>
</section>

<section class="services">
  <div class="placeholder" style="inset:0;background:linear-gradient(90deg,rgba(255,255,255,.06),rgba(255,255,255,0) 40%)" role="img" aria-label="Faint background photo of a person working"></div>
  <h2 class="section-title">Our <em>Services</em></h2>
  <div class="cards">
    <div class="svc">
      <svg width="70" height="70" viewBox="0 0 70 70" fill="none" stroke="#1a6fd0" stroke-width="2.2"><circle cx="26" cy="32" r="18"/><path d="M26 22v20M31 26c-2-2-9-2-9 2s9 2 9 6-7 4-9 2"/><path d="M46 66V50h12v16M44 66h16M48 50v-6h8v6M50 44v-4h4v4"/></svg>
      <h3>Digital<br>Strategy</h3>
      <p>Lorem ipsum dolor sit am consectetur adipiscinge sed do eiusmod sed.</p>
      <div class="arrow"><svg width="18" height="18" viewBox="0 0 18 18" fill="none" stroke="#fff" stroke-width="2"><path d="M3 9h12M10 4l5 5-5 5"/></svg></div>
    </div>
    <div class="svc featured">
      <svg width="70" height="70" viewBox="0 0 70 70" fill="none" stroke="#fff" stroke-width="2.2"><circle cx="35" cy="22" r="16"/><circle cx="35" cy="18" r="5"/><path d="M27 32c2-5 14-5 16 0"/><circle cx="16" cy="48" r="5"/><circle cx="35" cy="48" r="5"/><circle cx="54" cy="48" r="5"/><path d="M7 64c2-6 16-6 18 0M26 64c2-6 16-6 18 0M45 64c2-6 16-6 18 0"/></svg>
      <h3>Technical<br>Expertise</h3>
      <p>Lorem ipsum dolor sit am consectetur adipiscinge sed do eiusmod sed.</p>
      <div class="arrow"><svg width="18" height="18" viewBox="0 0 18 18" fill="none" stroke="#fff" stroke-width="2"><path d="M3 9h12M10 4l5 5-5 5"/></svg></div>
    </div>
    <div class="svc">
      <svg width="70" height="70" viewBox="0 0 70 70" fill="none" stroke="#1a6fd0" stroke-width="2.2"><circle cx="30" cy="30" r="22"/><circle cx="30" cy="30" r="15"/><path d="M23 36v-6M29 36V24M35 36v-9"/><path d="M46 48l8 8"/><path d="M40 64l10-8 6 4 10-10" stroke="#2a9c2f"/></svg>
      <h3>Data<br>Analytics</h3>
      <p>Lorem ipsum dolor sit am consectetur adipiscinge sed do eiusmod sed.</p>
      <div class="arrow"><svg width="18" height="18" viewBox="0 0 18 18" fill="none" stroke="#fff" stroke-width="2"><path d="M3 9h12M10 4l5 5-5 5"/></svg></div>
    </div>
    <div class="svc">
      <svg width="70" height="70" viewBox="0 0 70 70" fill="none" stroke="#1a6fd0" stroke-width="2.2"><path d="M32 10c-10 0-18 6-18 16 0 6-6 8-6 14s6 10 14 10c2 6 8 8 10 8z"/><path d="M32 10v48M22 24h10M18 36h14M24 46h8"/><path d="M32 20h14M32 32h20M32 44h14" stroke="#2a9c2f"/><circle cx="48" cy="20" r="3" stroke="#2a9c2f"/><circle cx="55" cy="32" r="3" stroke="#2a9c2f"/><circle cx="48" cy="44" r="3" stroke="#2a9c2f"/></svg>
      <h3>Artificial<br>Intelligence</h3>
      <p>Lorem ipsum dolor sit am consectetur adipiscinge sed do eiusmod sed.</p>
      <div class="arrow"><svg width="18" height="18" viewBox="0 0 18 18" fill="none" stroke="#fff" stroke-width="2"><path d="M3 9h12M10 4l5 5-5 5"/></svg></div>
    </div>
  </div>
  <div class="btn btn-blue" style="left:491px;top:593px;width:218px;height:52px">View All Services</div>
</section>

<section class="values">
  <div class="placeholder" style="left:88px;top:130px;width:275px;height:210px;border-radius:6px;background:linear-gradient(135deg,#2a2f36,#5a4d44)" role="img" aria-label="Photo of a woman in front of screens of code"></div>
  <div class="placeholder" style="left:370px;top:97px;width:138px;height:126px;border-radius:6px;background:linear-gradient(135deg,#ddd5cf,#8c7466)" role="img" aria-label="Photo of a woman talking on the phone"></div>
  <div class="placeholder" style="left:118px;top:236px;width:168px;height:155px;border-radius:6px;border:5px solid #fff;background:linear-gradient(135deg,#0b2a7a,#1f5ad8)" role="img" aria-label="Illustration of a glowing AI chip"></div>
  <h2 class="section-title">Our Values</h2>
  <p class="abs values-intro">Lorem ipsum dolor sit amet, consectetur adipis icing elitos sed do eiusmod tempor incidi dunt ut lab ore et dolore sed magna aliqua.</p>
  <div class="btn btn-green" style="left:88px;top:599px;width:157px;height:50px">View More</div>

  <div class="value" style="top:104px">
    <div class="circle" style="background:#e6f0fb;top:0">
      <svg width="52" height="52" viewBox="0 0 52 52" fill="none" stroke="#1a6fd0" stroke-width="2"><path d="M26 4c8 6 10 16 8 28H18c-2-12 0-22 8-28z"/><circle cx="26" cy="18" r="4"/><path d="M18 26l-7 8v6l7-4M34 26l7 8v6l-7-4M21 36l-1 10 6-4 6 4-1-10"/></svg>
    </div>
    <h4 style="top:-4px">Innovation</h4>
    <p style="top:25px">We are committed to staying at the forefront of digital transformation, continuously exploring new technologies and solutions that drive impactful change</p>
    <hr style="top:143px">
  </div>
  <div class="value" style="top:289px">
    <div class="circle" style="background:#e7f5e7;top:0">
      <svg width="54" height="54" viewBox="0 0 54 54" fill="none" stroke="#2a9c2f" stroke-width="2"><circle cx="27" cy="27" r="20"/><circle cx="27" cy="22" r="5"/><path d="M18 36c2-6 16-6 18 0"/><circle cx="13" cy="18" r="3"/><circle cx="41" cy="18" r="3"/><circle cx="13" cy="38" r="3"/><circle cx="41" cy="38" r="3"/></svg>
    </div>
    <h4 style="top:-10px">People-Driven</h4>
    <p style="top:19px">We work in collaboration with our clients, employing a customer-centric approach that puts people at the centre of what we do.</p>
    <hr style="top:131px">
  </div>
  <div class="value" style="top:464px">
    <div class="circle" style="background:#e6f0fb;top:0">
      <svg width="56" height="56" viewBox="0 0 56 56" fill="none" stroke="#1a6fd0" stroke-width="2"><circle cx="26" cy="30" r="18"/><circle cx="26" cy="30" r="10"/><circle cx="26" cy="30" r="3"/><path d="M26 30L48 8M42 8h6v6"/><path d="M26 8v-4M26 56v-4M4 30H0" /></svg>
    </div>
    <h4 style="top:-10px">Passionate</h4>
    <p style="top:19px">We're passionate about helping businesses live up to their full potential and grow beyond conventional market boundaries</p>
  </div>
</section>

<section class="products">
  <h2 class="section-title">Featured Products</h2>
  <div class="slide-btn" style="left:50px">
    <svg width="22" height="22" viewBox="0 0 22 22" fill="none" stroke="#fff" stroke-width="2"><path d="M18 11H4M9 6l-5 5 5 5"/></svg>
  </div>
  <div class="slide-btn" style="left:1084px">
    <svg width="22" height="22" viewBox="0 0 22 22" fill="none" stroke="#fff" stroke-width="2"><path d="M4 11h14M13 6l5 5-5 5"/></svg>
  </div>
  <div class="prod-row">
    <div class="prod">
      <div class="shot" style="background:linear-gradient(135deg,#2a2d33,#e9e9e9 60%,#3a3d42)" role="img" aria-label="Mock-ups of printed template layouts"></div>
      <h3>Templates</h3>
      <div class="stars"><svg width="90" height="14" viewBox="0 0 90 14" fill="#f2b01e"><path id="st" d="M7 0l2 5h5l-4 3 1.6 5L7 10l-4.6 3L4 8 0 5h5z"/><use href="#st" x="19"/><use href="#st" x="38"/><use href="#st" x="57"/><use href="#st" x="76"/></svg>(51)</div>
      <p>Lorem ipsum dolor sit am conse tetur adipiscinge sed do eius</p>
      <div class="rule"></div>
      <div class="price"><b>$67.00</b>/lifetime</div>
      <div class="buy">ADD TO CART</div>
    </div>
    <div class="prod">
      <div class="shot" style="background:linear-gradient(135deg,#eeeeee,#8a6d52 55%,#d9d5d0)" role="img" aria-label="Tablet showing an e-book on a wooden table"></div>
      <h3>e-books</h3>
      <div class="stars"><svg width="90" height="14" viewBox="0 0 90 14" fill="#f2b01e"><use href="#st"/><use href="#st" x="19"/><use href="#st" x="38"/><use href="#st" x="57"/><use href="#st" x="76"/></svg>(51)</div>
      <p>Lorem ipsum dolor sit am conse tetur adipiscinge sed do eius</p>
      <div class="rule"></div>
      <div class="price"><b>$20.00</b>/lifetime</div>
      <div class="buy solid">ADD TO CART</div>
    </div>
    <div class="prod">
      <div class="shot" style="background:linear-gradient(135deg,#d7e9f7,#6aa8dc 60%,#e6f1fa)" role="img" aria-label="Mobile app screens floating on a light background"></div>
      <h3>Software</h3>
      <div class="stars"><svg width="90" height="14" viewBox="0 0 90 14" fill="#f2b01e"><use href="#st"/><use href="#st" x="19"/><use href="#st" x="38"/><use href="#st" x="57"/><use href="#st" x="76"/></svg>(51)</div>
      <p>Lorem ipsum dolor sit am conse tetur adipiscinge sed do eius</p>
      <div class="rule"></div>
      <div class="price"><b>$67.00</b>/annual</div>
      <div class="buy">ADD TO CART</div>
    </div>
  </div>
</section>

<section class="team">
  <h2 class="section-title">Our Team</h2>
  <div class="btn btn-green" style="left:953px;top:98px;width:157px;height:49px">View More</div>
  <div class="member" style="left:75px">
    <div class="avatar" style="background:linear-gradient(160deg,#cfd3d8,#7c8896)" role="img" aria-label="Portrait of a team member in a striped shirt"></div>
    <h4>Jomo Kariuki</h4>
    <p>Lorem ipsum dolor sit am con tetur adipiscinge sed do</p>
  </div>
  <div class="member" style="left:341px">
    <div class="avatar" style="background:linear-gradient(180deg,#1a6fd0,#26a03a);display:flex;align-items:center;justify-content:center">
      <span style="width:60px;height:60px;border-radius:50%;border:2px solid #fff;display:block"></span>
    </div>
    <h4>Jomo Kariuki</h4>
    <p>Lorem ipsum dolor sit am con tetur adipiscinge sed do</p>
  </div>
  <div class="member" style="left:607px">
    <div class="avatar" style="background:linear-gradient(160deg,#e5e5e5,#5f6670)" role="img" aria-label="Portrait of a bearded team member"></div>
    <h4>Jomo Kariuki</h4>
    <p>Lorem ipsum dolor sit am con tetur adipiscinge sed do</p>
  </div>
  <div class="member" style="left:873px">
    <div class="avatar" style="background:linear-gradient(160deg,#f1efed,#8a5a45)" role="img" aria-label="Portrait of a smiling team member"></div>
    <h4>Jomo Kariuki</h4>
    <p>Lorem ipsum dolor sit am con tetur adipiscinge sed do</p>
  </div>
</section>

<footer class="site-footer">
  <div class="abs f-brand">
    <div class="brand-name">Tavi Linkway</div>
    <div class="brand-tag">A DIGITAL MARKETPLACE</div>
  </div>
  <div class="abs f-social"><span><i></i></span><span><i></i></span><span><i></i></span><span><i></i></span></div>

  <div class="f-col" style="left:374px">
    <h5>Quick Links</h5>
    <ul><li>Home</li><li>Services</li><li>Digital Marketplace</li><li>About Us</li><li>Blog</li><li>Contact</li></ul>
  </div>
  <div class="f-col" style="left:626px">
    <h5>Services</h5>
    <ul><li>Consulting Services</li><li>Technical Expertise</li><li>Advisory Solutions</li><li>Analytics</li><li>e-commerce</li></ul>
  </div>
  <div class="f-col" style="left:880px;width:232px">
    <h5>Contact Info</h5>
    <div class="contact-item" style="margin-top:20px">
      <svg width="18" height="14" viewBox="0 0 18 14" fill="none" stroke="#3fb13c" stroke-width="1.8"><rect x="1" y="1" width="16" height="12" rx="1.5"/><path d="M1 2l8 6 8-6"/></svg>
      <div>Email:<br>info@tavilinkway.com</div>
    </div>
    <div class="contact-item" style="margin-top:25px">
      <svg width="18" height="18" viewBox="0 0 18 18" fill="none" stroke="#3fb13c" stroke-width="1.8"><path d="M4 1.5l3 3.5-2 2c1 2.5 3 4.5 5.5 5.5l2-2 3.5 3-2 2.5C8 16 2 10 1.5 3.5z"/></svg>
      <div>Phone:<br>123-555-0147</div>
    </div>
    <div class="contact-item" style="margin-top:25px">
      <svg width="18" height="20" viewBox="0 0 18 20" fill="#fff"><path d="M9 0a7 7 0 0 0-7 7c0 5 7 13 7 13s7-8 7-13a7 7 0 0 0-7-7zm0 10a3 3 0 1 1 0-6 3 3 0 0 1 0 6z"/></svg>
      <div>Address:<br>48 Kilima Lane, Westlands<br>Rd. 00100</div>
    </div>
  </div>

  <div class="copyright">Copyright © 2024 Tavi Linkway. All rights reserved.</div>
</footer>

</body>
</html>
```